Design for mobile and web app for sweepstakes.

We need the design for a mobile app (planned to be build with jquery mobile) and web app (mobile first, we will use same look and feel as mobile just with displaying more info at once).

The following pages must be included:
- Userregistration/Login (Reg via Email, Chattrove-Reg)

- List of available sweepstakes (including some icons: a video icon, a "like button" type icon, a "provide some info" type of icon) this should be on the side in wep app but in mobile app its a list. possible is also a mobile display where users can swipe back and forth through it.

- single sweepstake detailview . should present a single sweepstake and give users the opportunity to participate with a button.

user settings. (doesnt not have to include a lot of fields we will at ourself. should contain some datepicker (birthday), some on/off switch (receive newsletters) some textfield in order for us to have a feel.

We have included the following files:
- glimmorica_logo_final01.png:
this is our logo which should be used and also the look and feel must fit with the logo.

- glimmorica_logo_final06.png:
this is the app-icon

-folie neu login registrierung :
this is a simple mockup for a registration page. the design doesnt have to contain all fields we will do that ourselfes starting from your handover, but should represent a common registration page with some fields

- funktionalität mit hässlichen buttons )
this is just a mockup for a possible design. not that it does use our old logo. This again is not binding is just to get a feel for what we are looking for. A list of sweepstakes and a detailspage for the sweepstake for users to participate in it.

Target Market(s)

German speaking users, Austria, Germany, Switzerland
The app is adressing a wide crowd of users who are interested in participating in sweepstakes.

Industry/Entity Type

Build

Number of Pages Required

4 page

Font styles to use
Sans Serif

Requirements
Must have
• - jquery and jquery mobile
• - html5 (preferable bootstrap-based)
• - css3
• - description on used fonts and colors. fonts must be free to use and publicly available for anyone to use.
• - all buttons should be css

```html
<!DOCTYPE html>
<html lang="de">
<head>
<meta charset="utf-8">
<title>glimmorica – Gewinnspiele</title>
<link rel="stylesheet" href="https://fonts.googleapis.com/css2?family=Kanit:wght@500;600&family=Questrial&display=swap">
<style>
  :root {
    --status-green: #93bf8a;
    --band-green-start: #8cb687;
    --band-green-end: #bfe0b6;
    --brand-green: #6a9b2c;
    --title-green: #6ea233;
    --tab-light: #6da22f;
    --tab-dark: #44651f;
    --text-dark: #3a3a3a;
    --date-blue: #1f7db3;
    --icon-grey: #6c6c6c;
    --field-bg: #fff8f8;
    --placeholder: #e0d6d6;
    --teal: #1bb69b;
    --orange: #f7a533;
    --navy: #1e3849;
    --white: #ffffff;
  }
  * { box-sizing: border-box; margin: 0; padding: 0; }
  html, body { width: 676px; height: 1200px; overflow: hidden; background: #eeeeee; }
  .app { position: relative; width: 676px; height: 1200px; overflow: hidden; background: #ececec; font-family: "Questrial", sans-serif; }

  .status-bar { position: absolute; top: 0; left: 0; width: 676px; height: 42px; background: var(--status-green); color: var(--white); font-family: "Questrial", sans-serif; font-size: 23px; }
  .status-bar .carrier { position: absolute; left: 12px; top: 8px; letter-spacing: 1px; }
  .status-bar .time { position: absolute; left: 0; width: 676px; text-align: center; top: 8px; }
  .status-bar .battery { position: absolute; right: 14px; top: 8px; display: flex; align-items: center; gap: 8px; }
  .status-bar svg { display: block; }

  .header { position: absolute; top: 42px; left: 0; width: 676px; height: 136px; background: linear-gradient(#ffffff, #f3f3f3); }
  .back-btn { position: absolute; left: 20px; top: 42px; }
  .brand { position: absolute; left: 0; width: 676px; top: 38px; text-align: center; font-family: "Kanit", sans-serif; font-weight: 600; font-size: 44px; color: var(--brand-green); letter-spacing: -0.5px; line-height: 1.2; }
  .menu-btn { position: absolute; right: 20px; top: 44px; width: 56px; }
  .menu-btn span { display: block; height: 12px; border-radius: 6px; background: var(--brand-green); margin-bottom: 7px; }

  .search-band { position: absolute; top: 178px; left: 0; width: 676px; height: 123px; background: linear-gradient(100deg, var(--band-green-start), var(--band-green-end)); }
  .search-field { position: absolute; left: 16px; top: 18px; width: 645px; height: 86px; background: var(--field-bg); border-radius: 3px; }
  .search-field .placeholder { position: absolute; left: 42px; top: 29px; font-size: 21px; color: var(--placeholder); }
  .search-field svg { position: absolute; right: 32px; top: 22px; }

  .sweep-list { position: absolute; top: 301px; left: 0; width: 676px; list-style: none; }
  .sweep-item { position: relative; height: 154px; background: var(--white); box-shadow: 0 3px 3px rgba(0,0,0,0.14); margin-bottom: 0; border-bottom: 2px solid #e2e2e2; }
  .sweep-art { position: absolute; left: 10px; top: 11px; width: 134px; height: 134px; border-radius: 50%; }
  .art-teal { background: var(--teal); }
  .art-orange { background: var(--orange); }
  .art-navy { background: var(--navy); }
  .sweep-title { position: absolute; left: 160px; top: 20px; font-family: "Kanit", sans-serif; font-weight: 500; font-size: 26px; color: var(--title-green); }
  .sweep-text { position: absolute; left: 160px; top: 60px; font-size: 21px; color: var(--text-dark); }
  .sweep-meta { position: absolute; left: 160px; top: 96px; font-family: "Kanit", sans-serif; font-weight: 500; font-size: 21px; color: var(--date-blue); }
  .sweep-meta .until { margin-right: 44px; }
  .sweep-actions { position: absolute; right: 10px; top: 60px; display: flex; align-items: flex-end; gap: 10px; }

  .tab-bar { position: absolute; left: 0; top: 1085px; width: 676px; height: 115px; display: flex; }
  .tab { flex: 1; display: flex; align-items: center; justify-content: center; font-family: "Kanit", sans-serif; font-weight: 500; font-size: 36px; color: var(--white); letter-spacing: 1px; }
  .tab-new { background: var(--tab-light); }
  .tab-all { background: var(--tab-dark); }
</style>
</head>
<body>
<div class="app">
  <div class="status-bar">
    <div class="carrier">●●●○○ VOXA</div>
    <div class="time">4:21 PM</div>
    <div class="battery">
      <span>22%</span>
      <svg width="40" height="20" viewBox="0 0 40 20"><rect x="1" y="1" width="34" height="18" rx="3" fill="none" stroke="#fff" stroke-width="2"/><rect x="4" y="4" width="7" height="12" fill="#fff"/><rect x="36" y="7" width="3" height="6" fill="#fff"/></svg>
    </div>
  </div>

  <header class="header">
    <svg class="back-btn" width="36" height="52" viewBox="0 0 36 52"><polyline points="30,4 8,26 30,48" fill="none" stroke="#6a9b2c" stroke-width="7" stroke-linecap="round" stroke-linejoin="round"/></svg>
    <div class="brand">glimmorica</div>
    <div class="menu-btn"><span></span><span></span><span></span></div>
  </header>

  <div class="search-band">
    <div class="search-field">
      <span class="placeholder">Type your text here......</span>
      <svg width="42" height="42" viewBox="0 0 42 42"><circle cx="17" cy="17" r="13" fill="none" stroke="#6a9b2c" stroke-width="3"/><path d="M10 15a8 8 0 0 1 6-6" fill="none" stroke="#6a9b2c" stroke-width="2"/><line x1="27" y1="27" x2="39" y2="39" stroke="#6a9b2c" stroke-width="4" stroke-linecap="round"/></svg>
    </div>
  </div>

  <ul class="sweep-list">
    <li class="sweep-item">
      <div class="sweep-art art-teal" role="img" aria-label="Illustration eines Lautsprechers"></div>
      <div class="sweep-title">Lorem Ipsum</div>
      <div class="sweep-text">Contrary to popular belief, Lorem</div>
      <div class="sweep-meta"><span class="until">Bis</span>2-12-2014</div>
      <div class="sweep-actions">
        <svg width="42" height="36" viewBox="0 0 42 36"><path d="M21 2 L2 19 L7 19 L7 34 L17 34 L17 24 L25 24 L25 34 L35 34 L35 19 L40 19 Z" fill="#6c6c6c"/><rect x="30" y="4" width="5" height="9" fill="#6c6c6c"/></svg>
        <svg width="32" height="32" viewBox="0 0 32 32"><rect x="1" y="13" width="7" height="18" rx="1" fill="#6c6c6c"/><path d="M10 14 L16 3 C19 2 20 5 19 8 L18 12 L28 12 C31 12 32 15 30 17 C32 19 31 21 29 22 C30 24 29 26 27 27 C28 29 26 31 24 31 L10 31 Z" fill="#6c6c6c"/></svg>
        <svg width="44" height="28" viewBox="0 0 44 28"><rect x="1" y="3" width="30" height="22" rx="2" fill="#6c6c6c"/><path d="M32 14 L43 4 L43 24 Z" fill="#6c6c6c"/><circle cx="9" cy="14" r="4" fill="#fff"/><circle cx="23" cy="14" r="4" fill="#fff"/><rect x="9" y="12" width="14" height="4" fill="#fff"/></svg>
      </div>
    </li>
    <li class="sweep-item">
      <div class="sweep-art art-orange" role="img" aria-label="Illustration eines Geschenks"></div>
      <div class="sweep-title">Lorem Ipsum</div>
      <div class="sweep-text">Contrary to popular belief, Lorem</div>
      <div class="sweep-meta"><span class="until">Bis</span>2-12-2014</div>
      <div class="sweep-actions">
        <svg width="42" height="36" viewBox="0 0 42 36"><path d="M21 2 L2 19 L7 19 L7 34 L17 34 L17 24 L25 24 L25 34 L35 34 L35 19 L40 19 Z" fill="#6c6c6c"/><rect x="30" y="4" width="5" height="9" fill="#6c6c6c"/></svg>
        <svg width="32" height="32" viewBox="0 0 32 32"><rect x="1" y="13" width="7" height="18" rx="1" fill="#6c6c6c"/><path d="M10 14 L16 3 C19 2 20 5 19 8 L18 12 L28 12 C31 12 32 15 30 17 C32 19 31 21 29 22 C30 24 29 26 27 27 C28 29 26 31 24 31 L10 31 Z" fill="#6c6c6c"/></svg>
        <svg width="44" height="28" viewBox="0 0 44 28"><rect x="1" y="3" width="30" height="22" rx="2" fill="#6c6c6c"/><path d="M32 14 L43 4 L43 24 Z" fill="#6c6c6c"/><circle cx="9" cy="14" r="4" fill="#fff"/><circle cx="23" cy="14" r="4" fill="#fff"/><rect x="9" y="12" width="14" height="4" fill="#fff"/></svg>
      </div>
    </li>
    <li class="sweep-item">
      <div class="sweep-art art-navy" role="img" aria-label="Illustration eines Smartphones"></div>
      <div class="sweep-title">Lorem Ipsum</div>
      <div class="sweep-text">Contrary to popular belief, Lorem</div>
      <div class="sweep-meta"><span class="until">Bis</span>2-12-2014</div>
      <div class="sweep-actions">
        <svg width="42" height="36" viewBox="0 0 42 36"><path d="M21 2 L2 19 L7 19 L7 34 L17 34 L17 24 L25 24 L25 34 L35 34 L35 19 L40 19 Z" fill="#6c6c6c"/><rect x="30" y="4" width="5" height="9" fill="#6c6c6c"/></svg>
        <svg width="32" height="32" viewBox="0 0 32 32"><rect x="1" y="13" width="7" height="18" rx="1" fill="#6c6c6c"/><path d="M10 14 L16 3 C19 2 20 5 19 8 L18 12 L28 12 C31 12 32 15 30 17 C32 19 31 21 29 22 C30 24 29 26 27 27 C28 29 26 31 24 31 L10 31 Z" fill="#6c6c6c"/></svg>
        <svg width="44" height="28" viewBox="0 0 44 28"><rect x="1" y="3" width="30" height="22" rx="2" fill="#6c6c6c"/><path d="M32 14 L43 4 L43 24 Z" fill="#6c6c6c"/><circle cx="9" cy="14" r="4" fill="#fff"/><circle cx="23" cy="14" r="4" fill="#fff"/><rect x="9" y="12" width="14" height="4" fill="#fff"/></svg>
      </div>
    </li>
    <li class="sweep-item">
      <div class="sweep-art art-navy" role="img" aria-label="Illustration einer Landkarte mit Standortmarke"></div>
      <div class="sweep-title">Lorem Ipsum</div>
      <div class="sweep-text">Contrary to popular belief, Lorem</div>
      <div class="sweep-meta"><span class="until">Bis</span>2-12-2014</div>
      <div class="sweep-actions">
        <svg width="42" height="36" viewBox="0 0 42 36"><path d="M21 2 L2 19 L7 19 L7 34 L17 34 L17 24 L25 24 L25 34 L35 34 L35 19 L40 19 Z" fill="#6c6c6c"/><rect x="30" y="4" width="5" height="9" fill="#6c6c6c"/></svg>
        <svg width="32" height="32" viewBox="0 0 32 32"><rect x="1" y="13" width="7" height="18" rx="1" fill="#6c6c6c"/><path d="M10 14 L16 3 C19 2 20 5 19 8 L18 12 L28 12 C31 12 32 15 30 17 C32 19 31 21 29 22 C30 24 29 26 27 27 C28 29 26 31 24 31 L10 31 Z" fill="#6c6c6c"/></svg>
        <svg width="44" height="28" viewBox="0 0 44 28"><rect x="1" y="3" width="30" height="22" rx="2" fill="#6c6c6c"/><path d="M32 14 L43 4 L43 24 Z" fill="#6c6c6c"/><circle cx="9" cy="14" r="4" fill="#fff"/><circle cx="23" cy="14" r="4" fill="#fff"/><rect x="9" y="12" width="14" height="4" fill="#fff"/></svg>
      </div>
    </li>
    <li class="sweep-item">
      <div class="sweep-art art-orange" role="img" aria-label="Illustration eines Siegertreppchens mit Sternen"></div>
      <div class="sweep-title">Lorem Ipsum</div>
      <div class="sweep-text">Contrary to popular belief, Lorem</div>
      <div class="sweep-meta"><span class="until">Bis</span>2-12-2014</div>
      <div class="sweep-actions">
        <svg width="42" height="36" viewBox="0 0 42 36"><path d="M21 2 L2 19 L7 19 L7 34 L17 34 L17 24 L25 24 L25 34 L35 34 L35 19 L40 19 Z" fill="#6c6c6c"/><rect x="30" y="4" width="5" height="9" fill="#6c6c6c"/></svg>
        <svg width="32" height="32" viewBox="0 0 32 32"><rect x="1" y="13" width="7" height="18" rx="1" fill="#6c6c6c"/><path d="M10 14 L16 3 C19 2 20 5 19 8 L18 12 L28 12 C31 12 32 15 30 17 C32 19 31 21 29 22 C30 24 29 26 27 27 C28 29 26 31 24 31 L10 31 Z" fill="#6c6c6c"/></svg>
        <svg width="44" height="28" viewBox="0 0 44 28"><rect x="1" y="3" width="30" height="22" rx="2" fill="#6c6c6c"/><path d="M32 14 L43 4 L43 24 Z" fill="#6c6c6c"/><circle cx="9" cy="14" r="4" fill="#fff"/><circle cx="23" cy="14" r="4" fill="#fff"/><rect x="9" y="12" width="14" height="4" fill="#fff"/></svg>
      </div>
    </li>
    <li class="sweep-item">
      <div class="sweep-art art-orange" role="img" aria-label="Illustration eines weiteren Gewinns"></div>
    </li>
  </ul>

  <nav class="tab-bar">
    <div class="tab tab-new">NEU</div>
    <div class="tab tab-all">ALLE</div>
  </nav>
</div>
</body>
</html>
```